FEATHER FOUR YONDER MENU REDESIGN *

Need to redesign existing menu to better explain concept. Need to highlight sauces and explain the process of choosing sauces,then homemade dips,then sides.

We would like to change the Menu from a Bi-Fold to a Tri-Fold, with Flavor Choices on the Middle Page.

Target Market(s)

Wing enthusiast

Industry/Entity Type

Fast Food Restaurant

Colors
6b449b
ffcf3e

Requirements
Must have
• Flavors prominently displayed.
• Clear, concise Step by Step Order Process.
• Choose your Flavor (Change the word “Sauce” to “Flavor”
• Combo or Pack?
• Choose your Dip
• Choose your Side Item
• Must have the Logo and the Tag Line: FEATHER FOUR YONDER -THE Spot To ROAM For Drums!
Nice to have
• Highlight the fact that Ranch and Blue Cheese Dips are made fresh daily.
• Fresh, never frozen Classic Chicken
• Every Order cooked to Order
• Skip the wait, order online

```html
<!DOCTYPE html>
<html lang="en">
<head>
<meta charset="utf-8">
<title>Feather Four Yonder Menu</title>
<link href="https://fonts.googleapis.com/css2?family=Alfa+Slab+One&family=Nunito:wght@700;800;900&family=Open+Sans:wght@400;600&family=Oswald:wght@300;500&display=swap" rel="stylesheet">
<style>
  :root {
    --purple: #77256f;
    --yellow: #ffc90a;
    --white: #ffffff;
    --mild: #7cc242;
    --hot: #ed1c24;
  }
  html, body { margin: 0; padding: 0; overflow: hidden; background: var(--white); }
  .menu {
    position: relative; width: 1200px; height: 933px; overflow: hidden;
    background: var(--white); color: var(--purple);
    font-family: "Open Sans", sans-serif;
  }
  .abs { position: absolute; }
  .slab { font-family: "Alfa Slab One", serif; font-weight: 400; }

  .food-backdrop {
    position: absolute; left: 0; top: 300px; width: 795px; height: 633px;
    background:
      radial-gradient(ellipse at 28% 55%, rgba(214,120,90,0.22), rgba(255,255,255,0) 60%),
      radial-gradient(ellipse at 75% 40%, rgba(190,110,80,0.14), rgba(255,255,255,0) 55%),
      linear-gradient(180deg, rgba(255,255,255,1) 0%, rgba(250,236,230,0.6) 40%, rgba(255,255,255,0.9) 100%);
  }

  .band { position: absolute; top: 70px; height: 87px; background: var(--yellow); }
  .band-left { left: 0; width: 408px; }
  .band-mid { left: 410px; width: 384px; }
  .band-right { left: 796px; width: 404px; }

  .brand { position: absolute; left: 24px; top: 84px; display: flex; align-items: center; gap: 10px; }
  .brand-dot { width: 16px; height: 16px; border-radius: 50%; background: var(--purple); }
  .brand-name { font-family: "Alfa Slab One", serif; font-size: 19px; line-height: 1; color: var(--purple); white-space: nowrap; }

  .steps { left: 50px; top: 112px; font-family: "Alfa Slab One", serif; font-size: 14px; line-height: 20px; }

  .head-small { font-family: "Alfa Slab One", serif; font-size: 27px; letter-spacing: 1px; line-height: 1; }
  .head-big { font-family: "Alfa Slab One", serif; line-height: 1; }

  .section-title { left: 0; width: 408px; top: 208px; text-align: center; font-size: 30px; }
  .style-bar { left: 0; top: 254px; width: 408px; height: 48px; background: var(--purple); color: var(--white);
    font-family: "Oswald", sans-serif; font-weight: 500; font-size: 24px; letter-spacing: 4px;
    display: flex; align-items: center; justify-content: center; }

  .combo { position: absolute; left: 64px; width: 310px; height: 42px; }
  .combo-count { position: absolute; top: 0; right: 254px; height: 40px; min-width: 38px; padding: 0 2px; box-sizing: border-box;
    background: var(--yellow); border-radius: 3px; font-family: "Alfa Slab One", serif; font-size: 31px; line-height: 40px; text-align: center; }
  .combo-info { position: absolute; left: 64px; top: 1px; font-size: 10.5px; line-height: 13.5px; text-transform: uppercase; }
  .combo-price { position: absolute; right: 0; top: 4px; font-family: "Alfa Slab One", serif; font-size: 27px; line-height: 1; }

  .divider { left: 0; top: 520px; width: 408px; height: 4px; background: var(--purple); }

  .pack { position: absolute; left: 60px; width: 314px; }
  .pack-row { display: flex; align-items: flex-end; }
  .pack-name { background: var(--purple); color: var(--yellow); font-family: "Alfa Slab One", serif; font-size: 21px;
    line-height: 32px; padding: 0 6px; border-radius: 3px; white-space: nowrap; }
  .leader { flex: 1; border-bottom: 3px dotted var(--purple); margin: 0 10px 9px; }
  .pack-price { font-family: "Alfa Slab One", serif; font-size: 21px; line-height: 30px; }
  .pack-note { font-size: 11.5px; margin-top: 6px; text-transform: uppercase; }

  .flavors-label { left: 409px; top: 172px; width: 382px; height: 26px; }
  .flavors-label .mark { position: absolute; left: 0; top: 4px; width: 24px; height: 18px; background: var(--purple); }
  .flavors-label .word { position: absolute; left: 29px; top: -4px; font-family: "Oswald", sans-serif; font-weight: 500; font-size: 23px; letter-spacing: 2px; }
  .flavors-label .rule { position: absolute; left: 140px; top: 3px; width: 242px; height: 18px; background: var(--purple); }
  .heat-note { left: 438px; top: 202px; font-family: "Oswald", sans-serif; font-weight: 300; font-size: 13.5px; }
  .heat-note .mild { color: var(--mild); font-weight: 500; }
  .heat-note .hot { color: var(--hot); font-weight: 500; }

  .flavor { position: absolute; left: 591px; font-family: "Nunito", sans-serif; font-weight: 900; font-size: 21px; line-height: 1; transform: translateY(-50%); }
  .flavor-icon { position: absolute; left: 436px; width: 40px; height: 40px; border-radius: 50%; background: var(--purple); opacity: 0.9; transform: translateY(-50%); }

  .price-line { position: absolute; left: 816px; width: 330px; display: flex; align-items: flex-end;
    font-family: "Alfa Slab One", serif; font-size: 19px; line-height: 24px; }
  .price-line .leader { margin: 0 6px 6px; border-bottom-width: 3px; }
  .dip-options { left: 816px; top: 211px; font-family: "Nunito", sans-serif; font-weight: 800; font-size: 15.5px; }

  .side-band { left: 791px; top: 338px; width: 409px; height: 87px; background: var(--yellow); }

  .side-title { position: absolute; left: 821px; font-family: "Alfa Slab One", serif; font-size: 16px; line-height: 1; letter-spacing: 0.3px; }
  .side-line { position: absolute; left: 821px; width: 321px; font-size: 12.8px; line-height: 1; display: flex; justify-content: space-between; }
  .side-line .dotted { flex: 1; border-bottom: 1px dotted var(--purple); margin: 0 3px 3px; }
  .roll-badge { position: absolute; top: 770px; height: 26px; background: var(--yellow); border-radius: 3px;
    font-family: "Alfa Slab One", serif; font-size: 20px; line-height: 26px; text-align: center; }
  .roll-price { position: absolute; top: 778px; font-size: 12.8px; }
</style>
</head>
<body>
<main class="menu">

  <div class="food-backdrop" role="img" aria-label="Soft faded photo of a plate of glazed chicken wings with celery and dip"></div>

  <div class="band band-left"></div>
  <div class="band band-mid"></div>
  <div class="band band-right"></div>

  <div class="brand"><span class="brand-dot"></span><span class="brand-name">FEATHER FOUR YONDER</span></div>
  <div class="abs steps">Order in 3 steps!<br>FLAVOR - DIPS - SIDES</div>

  <div class="abs" style="left:438px; top:78px;">
    <div class="head-small">CHOOSE YOUR</div>
    <div class="head-big" style="font-size:44px; letter-spacing:4px; margin-top:6px;">FLAVOR</div>
  </div>
  <div class="abs" style="left:809px; top:81px;">
    <div class="head-small">CHOOSE YOUR</div>
    <div class="head-big" style="font-size:30px; letter-spacing:3px; margin-top:8px;">HOMEMADE DIPS</div>
  </div>

  <div class="abs slab section-title">COMBOS &amp; PACKS</div>
  <div class="abs style-bar">CLASSIC&nbsp; OR&nbsp; BONELESS</div>

  <div class="combo" style="top:341px;">
    <div class="combo-count">6</div>
    <div class="combo-info">2 Flavors, 1 Dip<br>Choice of 1 Side<br><span style="text-transform:none">20 oz</span> DRINK</div>
    <div class="combo-price">$8.49</div>
  </div>
  <div class="combo" style="top:396px;">
    <div class="combo-count">8</div>
    <div class="combo-info">2 Flavors, 1 Dip<br>Choice of 1 Side<br><span style="text-transform:none">20 oz</span> DRINK</div>
    <div class="combo-price">$9.89</div>
  </div>
  <div class="combo" style="top:451px;">
    <div class="combo-count">12</div>
    <div class="combo-info">2 Flavors, 2 Dips<br>Choice of 1 Side<br><span style="text-transform:none">20 oz</span> DRINK</div>
    <div class="combo-price">$14.49</div>
  </div>

  <div class="abs divider"></div>

  <div class="pack" style="top:552px;">
    <div class="pack-row"><span class="pack-name">24 Pack</span><span class="leader"></span><span class="pack-price">$26.29</span></div>
    <div class="pack-note">3 Flavors, 3 Dips, Choice of 1 Side, Veggie Stix</div>
  </div>
  <div class="pack" style="top:618px;">
    <div class="pack-row"><span class="pack-name">30 Pack</span><span class="leader"></span><span class="pack-price">$32.99</span></div>
    <div class="pack-note">3 Flavors, 3 Dips, Choice of 1 Side, Veggie Stix</div>
  </div>
  <div class="pack" style="top:684px;">
    <div class="pack-row"><span class="pack-name">40 Pack</span><span class="leader"></span><span class="pack-price">$41.99</span></div>
    <div class="pack-note">4 Flavors, 4 Dips, Choice of 1 Side, 2 Veggie Stix</div>
  </div>
  <div class="pack" style="top:750px;">
    <div class="pack-row"><span class="pack-name">50 Pack</span><span class="leader"></span><span class="pack-price">$48.99</span></div>
    <div class="pack-note">4 Flavors, 4 Dips, 2 Large Side, 2 Veggie Stix</div>
  </div>
  <div class="pack" style="top:815px;">
    <div class="pack-row"><span class="pack-name">100 Pack</span><span class="leader"></span><span class="pack-price">$94.99</span></div>
    <div class="pack-note">6 Flavors, 8 Dips, 4 Large Sides, 4 Veggie Stix</div>
  </div>

  <div class="abs flavors-label"><span class="mark"></span><span class="word">FLAVORS</span><span class="rule"></span></div>
  <div class="abs heat-note">listed in heat increments from <span class="mild">mildest</span> to <span class="hot">hottest</span></div>

  <svg class="abs" style="left:490px; top:240px;" width="100" height="640" viewBox="490 240 100 640" aria-hidden="true">
    <defs>
      <linearGradient id="heat" x1="0" y1="0" x2="0" y2="1">
        <stop offset="0" stop-color="#ed1c24"/>
        <stop offset="0.3" stop-color="#f7941d"/>
        <stop offset="0.52" stop-color="#ffc90a"/>
        <stop offset="0.78" stop-color="#7cc242"/>
        <stop offset="1" stop-color="#1cb5e0"/>
      </linearGradient>
    </defs>
    <path d="M534 250 c-10 8 -14 18 -8 28 c-8 -2 -10 -8 -8 -14 c-6 8 -6 20 6 24 h20 c10 -6 8 -18 0 -24 c2 6 0 10 -4 12 c4 -10 0 -20 -6 -26 z" fill="var(--hot)"/>
    <path d="M520 294 h32 v518 a32 32 0 1 1 -32 0 z" fill="var(--white)" stroke="var(--purple)" stroke-width="4"/>
    <rect x="526" y="300" width="20" height="520" fill="url(#heat)"/>
    <circle cx="536" cy="838" r="26" fill="#1cb5e0"/>
    <g stroke="var(--purple)" stroke-width="3">
      <line x1="504" y1="316" x2="520" y2="316"/><line x1="552" y1="316" x2="566" y2="316"/><line x1="572" y1="316" x2="578" y2="316"/>
      <line x1="504" y1="370" x2="520" y2="370"/><line x1="552" y1="370" x2="566" y2="370"/><line x1="572" y1="370" x2="578" y2="370"/>
      <line x1="504" y1="424" x2="520" y2="424"/><line x1="552" y1="424" x2="566" y2="424"/><line x1="572" y1="424" x2="578" y2="424"/>
      <line x1="504" y1="478" x2="520" y2="478"/><line x1="552" y1="478" x2="566" y2="478"/><line x1="572" y1="478" x2="578" y2="478"/>
      <line x1="504" y1="531" x2="520" y2="531"/><line x1="552" y1="531" x2="566" y2="531"/><line x1="572" y1="531" x2="578" y2="531"/>
      <line x1="504" y1="586" x2="520" y2="586"/><line x1="552" y1="586" x2="566" y2="586"/><line x1="572" y1="586" x2="578" y2="586"/>
      <line x1="504" y1="639" x2="520" y2="639"/><line x1="552" y1="639" x2="566" y2="639"/><line x1="572" y1="639" x2="578" y2="639"/>
      <line x1="504" y1="693" x2="520" y2="693"/><line x1="552" y1="693" x2="566" y2="693"/><line x1="572" y1="693" x2="578" y2="693"/>
      <line x1="504" y1="746" x2="520" y2="746"/><line x1="552" y1="746" x2="566" y2="746"/><line x1="572" y1="746" x2="578" y2="746"/>
      <line x1="504" y1="800" x2="520" y2="800"/><line x1="552" y1="800" x2="566" y2="800"/><line x1="572" y1="800" x2="578" y2="800"/>
    </g>
  </svg>

  <div class="flavor-icon" style="top:316px;" role="img" aria-label="Lightning bolt icon"></div>
  <div class="flavor-icon" style="top:370px;" role="img" aria-label="Mango icon"></div>
  <div class="flavor-icon" style="top:424px;" role="img" aria-label="Flaming pepper icon"></div>
  <div class="flavor-icon" style="top:478px;" role="img" aria-label="Lime and chili icon"></div>
  <div class="flavor-icon" style="top:531px;" role="img" aria-label="Buffalo icon"></div>
  <div class="flavor-icon" style="top:586px;" role="img" aria-label="Lemon icon"></div>
  <div class="flavor-icon" style="top:639px;" role="img" aria-label="Mild letter badge icon"></div>
  <div class="flavor-icon" style="top:693px;" role="img" aria-label="Garlic icon"></div>
  <div class="flavor-icon" style="top:746px;" role="img" aria-label="Grill icon"></div>
  <div class="flavor-icon" style="top:800px;" role="img" aria-label="Chopsticks icon"></div>

  <div class="flavor" style="top:316px;">Blazin'</div>
  <div class="flavor" style="top:370px;">Mango Habanero</div>
  <div class="flavor" style="top:424px;">Cajun</div>
  <div class="flavor" style="top:478px;">Sweet Thai Chili</div>
  <div class="flavor" style="top:531px;">Buffalo</div>
  <div class="flavor" style="top:586px;">Lemon Pepper</div>
  <div class="flavor" style="top:639px;">Mild</div>
  <div class="flavor" style="top:693px;">Garlic Parm</div>
  <div class="flavor" style="top:746px;">BBQ</div>
  <div class="flavor" style="top:800px;">Teriyaki</div>

  <div class="price-line" style="top:186px;"><span>Dips</span><span class="leader"></span><span>$0.79</span></div>
  <div class="abs dip-options">Ranch | Blue Cheese | Honey Mustard</div>
  <div class="price-line" style="top:249px;"><span>Cheese Sauce</span><span class="leader"></span><span>$1.00</span></div>

  <div class="abs side-band"></div>
  <div class="abs" style="left:822px; top:347px;">
    <div class="head-small">CHOOSE YOUR</div>
    <div class="head-big" style="font-size:42px; letter-spacing:5px; margin-top:6px;">SIDE ITEM</div>
  </div>

  <div class="side-title" style="top:466px;">WAFFLE FRIES SEASONED</div>
  <div class="side-line" style="top:491px;"><span>SMALL ......... $2.79</span><span>LARGE ......... $4.29</span></div>
  <div class="side-line" style="top:510px;"><span>ADD CHEESE SAUCE</span><span class="dotted"></span><span>$1.00</span></div>

  <div class="side-title" style="top:542px;">VEGGIE STIX</div>
  <div class="side-line" style="top:544px; left:955px; width:187px;"><span class="dotted"></span><span>$0.89</span></div>

  <div class="side-title" style="top:575px;">COLESLAW</div>
  <div class="side-line" style="top:600px;"><span>SMALL ......... $1.99</span><span>LARGE ......... $3.59</span></div>

  <div class="side-title" style="top:632px;">BAKED BEANS</div>
  <div class="side-line" style="top:657px;"><span>SMALL ......... $1.99</span></div>
  <div class="side-line" style="top:662px; justify-content:flex-end;"><span>LARGE ......... $3.59</span></div>

  <div class="side-title" style="top:690px;">POTATO SALAD</div>
  <div class="side-line" style="top:716px;"><span>SMALL ......... $1.99</span><span>LARGE ......... $3.59</span></div>

  <div class="side-title" style="top:746px;">ROLLS</div>
  <div class="roll-badge" style="left:821px; width:26px;">1</div>
  <div class="roll-price" style="left:853px;">$0.49</div>
  <div class="roll-badge" style="left:922px; width:28px;">6</div>
  <div class="roll-price" style="left:955px;">$2.99</div>
  <div class="roll-badge" style="left:1018px; width:46px;">12</div>
  <div class="roll-price" style="left:1070px;">$5.59</div>

  <div class="side-title" style="top:816px;">FOUNTAIN DRINKS</div>
  <div class="side-line" style="top:840px;"><span>20 oz &nbsp;......... $1.99</span><span>32 oz ......... $2.59</span></div>

</main>
</body>
</html>
```